ARTM Website and Inner page template

Home page website design with inner page design for template. Details below as well as in txt document included
Project Description: New website for a current client ( ARTM ) .. current website is located at https://www.artmhub.org/Home.aspx
I need a home page design with an inner page design that will be used as a template ( 2 pages )
Logo is attached
Important notes:
Every page has to include the mission and vision. See below
"Our mission: to protect the public by promoting excellence in chiropractic regulation through service to our member boards
Our vision: The ARTM is the premier international resource for information and consolidated services for ensuring the safe, ethical practice of chiropractic"
Social media icons on the head of every page
chatterbox
flitter
workloop
snapgrid
clipstream
Every page needs to include the phone number on the header and footer
Main navigation links ( they are going to be different from current website ). Since most of these links are going to have sub-menus, please show the rollover affect. I have included the sub-menu options for "Get Started". The sub-menu should not be in a "list style" because the sub-menu links are categorized in some cases. A good example on their current website is to roll over the "Services" link in the main navigation
"Get Started" Sub-menu options ( categories and links )
- Chiropractic Regulators
- Annual Meeting
- District Meetings
- Licensing Board Information
- Library
- Administrators ( DRNEV )
- Legal Advisors ( DRNEV )
- Other Chiropractic Organizations
- Chiropractic Patients
- How to check a license
- Look up a license
- Request a Disciplinary Report
- Consumer Information
- Registered Chiropractors & Chiropractic Assistants
- Continuing Education Courses
- Chiropractic Assistant
- Certification
- View your continuing Ed Credits
Full list if primary navigation links:
Home
Contact
Company Info
Chiropractic Boards
Resources
Services
Get Started
Home Page Specifics:
"Hero Banner" or large "Slider" image with text at top of page below main navigation
4 primary points of interest to highlight
- MOR-TEP ( mutual oversight registry tracking enforcement portal )
- VOLT ( Vetted Organizers of Learning Tracks )
- RHLT ( Registered Health Liaison Technicians )
- Keystone ( Openly Indexed Spinal Listings )
Large "Member Access" area with the following links inside it
- Register for meetings
- Pay an Invoice
- MOR-TEP
- VOLT
- RHLT
- Report to MOR-TEP
- DRNEV Login
Large "Get Started" section with 3 categories that have links
- Chiropractic Regulators
- Annual Meeting
- District Meetings
- Library
- Chiropractic Patients
- How to Check a license
- Look up a license
- Consumer Information
- Coninuing Education Courses
- Chiropractic Assistant
- Certification
- View Your Continuing Ed Credits
Inner page specifics:
The inner page should look similar to the home page at the header and footer areas then have a large area for content. No large images or anything like that needed..
IMPORTANT... ONLY USE GRAPHICS/IMAGES from pixmarble. ( https://www.pixmarble.com/ ) This is important because we have an account with them so you can use the watermarked images then when I build the website I can easily purchase the licensing rights for those images. You dont' need an account to do searches, locate images and use the water marked image in the design.
Target Market(s)
Chiropractic Licensing
Number of Pages Required
2 page
Requirements
Must have
- Please see attached document
Nice to have
Should not have

```html
<!DOCTYPE html>
<html lang="en">
<head>
<meta charset="utf-8">
<title>ARTM – Home</title>
<link href="https://fonts.googleapis.com/css2?family=Poppins:wght@400;500;600&family=Prata&display=swap" rel="stylesheet">
<style>
:root{
  --topbar:#1690ea;
  --topbar-dark:#2f679e;
  --navy:#2e6399;
  --btn:#2d5f93;
  --bright:#1593ec;
  --ink:#1d1d1d;
  --muted:#555;
  --soft:#f4f4f4;
  --panel:#efefef;
  --link:#1d4f86;
}
*{box-sizing:border-box;margin:0;padding:0}
html,body{width:1200px;height:3038px;overflow:hidden}
body{font-family:"Poppins",sans-serif;color:var(--ink);background:#fff;position:relative}
.serif{font-family:"Prata",serif;font-weight:400}
a{color:inherit;text-decoration:none}
.btn{display:inline-block;background:var(--btn);color:#fff;font-size:15px;font-weight:500;letter-spacing:.3px;padding:0 19px;height:37px;line-height:37px;border-radius:6px}

/* top bar */
.topbar{position:absolute;top:0;left:0;width:1200px;height:38px;background:var(--topbar);color:#fff;font-size:13px}
.topbar .mail{position:absolute;left:60px;top:0;height:38px;display:flex;align-items:center;gap:14px}
.topbar .phone{position:absolute;right:0;top:0;width:203px;height:38px;background:var(--topbar-dark);display:flex;align-items:center;gap:20px;padding-left:22px;font-weight:600;font-size:15px}

/* header */
.header{position:absolute;top:38px;left:0;width:1200px;height:78px;background:#fff}
.brand{position:absolute;left:60px;top:14px;display:flex;align-items:center;gap:10px}
.brand .mark{width:50px;height:50px;background:var(--navy)}
.brand .name{font-family:"Prata",serif;font-size:30px;color:var(--navy)}
.nav{position:absolute;left:433px;top:26px;display:flex;font-size:12.5px;color:#444}
.nav a{padding:0 11px;height:34px;line-height:34px;white-space:nowrap}
.nav a.active{background:#e7f1fb;color:var(--bright);border-radius:17px}
.header .btn{position:absolute;left:1004px;top:22px}

/* hero */
.hero{position:absolute;top:116px;left:0;width:1200px;height:637px;background:linear-gradient(100deg,#c9cbcf 0%,#b9b7b5 30%,#e1dfdc 55%,#e9e8e6 80%,#d7d4cb 100%)}
.hero-copy{position:absolute;right:60px;top:214px;text-align:right}
.hero-copy h1{font-size:47px;line-height:52px;color:#111}
.hero-copy .btn{margin-top:27px}

/* quicklinks */
.quick{position:absolute;top:753px;left:0;width:1200px;height:353px;background:var(--soft)}
.section-title{text-align:center;font-size:25px;color:#111}
.section-title .accent{color:var(--navy)}
.quick .section-title{margin-top:72px}
.quick-row{display:flex;position:absolute;top:130px;left:48px}
.quick-item{width:276px;text-align:center}
.quick-item .badge{width:56px;height:56px;border-radius:50%;margin:0 auto;background:#dfe5ee}
.quick-item h3{font-weight:400;font-size:19px;margin-top:25px;color:#111}
.quick-item p{font-size:13px;line-height:20px;color:#333;margin-top:6px;padding:0 14px}

/* member access */
.members{position:absolute;top:1106px;left:0;width:1200px;height:534px}
.members .section-title{margin-top:80px}
.access{position:absolute;width:260px;text-align:center;transform:translateX(-50%)}
.access .ring{width:90px;height:90px;border-radius:50%;background:var(--bright);margin:0 auto;border:5px solid #cfe7fb;display:flex;align-items:center;justify-content:center}
.access span{display:block;margin-top:19px;font-size:17px;color:#111}

/* get started grid */
.grid{position:absolute;top:1640px;left:60px;width:1080px;height:750px;display:grid;grid-template-columns:360px 360px 360px;grid-template-rows:375px 375px}
.photo{width:100%;height:100%}
.panel{background:var(--panel);display:flex;flex-direction:column;align-items:center;justify-content:center;text-align:center}
.panel h2{font-size:20px;color:#111;margin-bottom:14px}
.panel .link{font-size:12.5px;color:var(--link);text-decoration:underline;line-height:30px}
.panel .btn{color:#fff;text-decoration:none;margin-top:26px;font-size:14.5px;line-height:37px}

/* contact strip */
.contact{position:absolute;top:2467px;left:0;width:1200px;height:100px}
.c-item{position:absolute;display:flex;gap:20px}
.c-item .ico{width:52px;height:52px;border-radius:50%;background:#edf0f4;display:flex;align-items:center;justify-content:center;flex:none}
.c-item h4{font-family:"Prata",serif;font-weight:400;font-size:17px;color:#111;margin-top:2px}
.c-item p{font-size:13.5px;color:#555;margin-top:9px;line-height:26px}

/* footer */
.footer{position:absolute;top:2624px;left:0;width:1200px;height:414px;background:var(--navy);color:#fff}
.f-brand{position:absolute;left:60px;top:62px;display:flex;align-items:center;gap:10px}
.f-brand .mark{width:50px;height:50px;background:#fff}
.f-brand .name{font-family:"Prata",serif;font-size:30px}
.f-mission{position:absolute;left:61px;top:148px;width:250px;font-size:12.5px;line-height:20px}
.f-col{position:absolute;top:60px}
.f-col h5{font-family:"Prata",serif;font-weight:400;font-size:19px;margin-bottom:22px}
.f-col a{display:block;font-size:12.5px;line-height:30px}
.f-sub{display:flex;width:252px;height:37px;background:#fff;align-items:center;gap:14px;padding-left:10px;color:#777;font-size:11.5px}
.f-col .btn{display:inline-block;background:var(--bright);margin-top:22px;font-size:15px;line-height:37px}
.copy{position:absolute;left:61px;top:384px;font-size:12px}
.social{position:absolute;right:60px;top:384px;font-size:12px;display:flex;gap:12px}
</style>
</head>
<body>

<div class="topbar">
  <div class="mail">
    <svg width="20" height="14" viewBox="0 0 20 14" fill="none" stroke="#fff" stroke-width="1.6"><rect x="1" y="1" width="18" height="12"/><path d="M1 1l9 7 9-7"/></svg>
    info@artmlicensingboards.org
  </div>
  <div class="phone">
    <svg width="20" height="20" viewBox="0 0 24 24" fill="#fff"><path d="M6.6 10.8c1.4 2.8 3.8 5.1 6.6 6.6l2.2-2.2c.3-.3.7-.4 1-.2 1.1.4 2.3.6 3.6.6.6 0 1 .4 1 1V20c0 .6-.4 1-1 1C10.6 21 3 13.4 3 4c0-.6.4-1 1-1h3.5c.6 0 1 .4 1 1 0 1.3.2 2.5.6 3.6.1.3 0 .7-.2 1z"/></svg>
    555.218.4400
  </div>
</div>

<header class="header">
  <div class="brand"><div class="mark"></div><div class="name">ARTM</div></div>
  <nav class="nav">
    <a class="active">Home</a><a>Company Info</a><a>Chiropractic Boards</a><a>Resources</a><a>Services</a><a>Contact</a>
  </nav>
  <a class="btn">GET STARTED</a>
</header>

<section class="hero" role="img" aria-label="Photo of a chiropractor adjusting a seated patient's neck in a bright clinic with a spine model">
  <div class="hero-copy">
    <h1 class="serif">The Public by Promoting<br>Excellence in Chiropractic<br>Regulation</h1>
    <a class="btn">GET STARTED</a>
  </div>
</section>

<section class="quick">
  <h2 class="section-title serif">ARTM Services <span class="accent">- Quicklinks</span></h2>
  <div class="quick-row">
    <div class="quick-item"><div class="badge"></div><h3>MOR-TEP</h3><p>Mutual Oversight Registry Tracking Enforcement Portal</p></div>
    <div class="quick-item"><div class="badge"></div><h3>VOLT</h3><p>Vetted Organizers of Learning Tracks</p></div>
    <div class="quick-item"><div class="badge"></div><h3>RHLT</h3><p>Registered Health Liaison Technicians</p></div>
    <div class="quick-item"><div class="badge"></div><h3>Keystone</h3><p>Openly Indexed Spinal Listings</p></div>
  </div>
</section>

<section class="members">
  <h2 class="section-title serif">Member Access</h2>
  <div class="access" style="left:186px;top:138px"><div class="ring"><svg width="40" height="40" viewBox="0 0 40 40" fill="none" stroke="#fff" stroke-width="2"><rect x="4" y="5" width="32" height="20" rx="2"/><path d="M9 11h22M9 17h22"/><path d="M19 23v12M15 29h8"/></svg></div><span class="serif">Register for meetings</span></div>
  <div class="access" style="left:461px;top:138px"><div class="ring"><svg width="40" height="40" viewBox="0 0 40 40" fill="none" stroke="#fff" stroke-width="2"><rect x="6" y="8" width="28" height="22" rx="2"/><rect x="13" y="4" width="14" height="20"/><path d="M16 10h8M16 14h8M16 18h8M12 34h16"/></svg></div><span class="serif">Pay an Invoice</span></div>
  <div class="access" style="left:737px;top:138px"><div class="ring"><svg width="40" height="40" viewBox="0 0 40 40" fill="none" stroke="#fff" stroke-width="2"><path d="M20 4v32"/><rect x="16" y="6" width="8" height="5" rx="2"/><rect x="16" y="14" width="8" height="5" rx="2"/><rect x="16" y="22" width="8" height="5" rx="2"/><rect x="16" y="30" width="8" height="5" rx="2"/></svg></div><span class="serif">MOR-TEP</span></div>
  <div class="access" style="left:1013px;top:138px"><div class="ring"><svg width="40" height="40" viewBox="0 0 40 40" fill="none" stroke="#fff" stroke-width="2"><rect x="12" y="5" width="24" height="18" rx="2"/><path d="M17 11h14M17 16h10"/><circle cx="9" cy="18" r="3"/><path d="M4 34v-8h10v8"/></svg></div><span class="serif">VOLT</span></div>
  <div class="access" style="left:324px;top:310px"><div class="ring"><svg width="40" height="40" viewBox="0 0 40 40" fill="none" stroke="#fff" stroke-width="2"><path d="M10 4h15l6 6v26H10z"/><path d="M14 14h12M14 19h12M14 24h8"/><circle cx="20" cy="30" r="3"/></svg></div><span class="serif">RHLT</span></div>
  <div class="access" style="left:601px;top:310px"><div class="ring"><svg width="40" height="40" viewBox="0 0 40 40" fill="none" stroke="#fff" stroke-width="2"><rect x="9" y="4" width="22" height="32" rx="3"/><circle cx="20" cy="13" r="4"/><path d="M14 30v-6M20 30v-9M26 30v-4"/></svg></div><span class="serif">Report to MOR-TEP</span></div>
  <div class="access" style="left:877px;top:310px"><div class="ring"><svg width="40" height="40" viewBox="0 0 40 40" fill="none" stroke="#fff" stroke-width="2"><rect x="5" y="7" width="30" height="24" rx="2"/><path d="M5 13h30"/><circle cx="20" cy="20" r="3"/><path d="M13 27h14"/></svg></div><span class="serif">DRNEV Login</span></div>
</section>

<section class="grid">
  <div class="photo" role="img" aria-label="Photo of a therapist in green scrubs holding a man's head and shoulder" style="background:linear-gradient(120deg,#9fa5a6 0%,#d9d8d4 55%,#5bb2a8 100%)"></div>
  <div class="panel">
    <h2 class="serif">Chiropractic Patients</h2>
    <a class="link">How to Check a license</a><a class="link">Look up a license</a><a class="link">Request a Disciplinary Report</a><a class="link">Consumer Information</a>
    <a class="btn">GET STARTED</a>
  </div>
  <div class="photo" role="img" aria-label="Photo of a chiropractor examining a woman's shoulder from behind" style="background:linear-gradient(120deg,#d4d4d4 0%,#b9a79c 45%,#6d5c7e 70%,#2f8f82 100%)"></div>
  <div class="panel">
    <h2 class="serif">Chiropractic Regulators</h2>
    <a class="link">Annual Meeting</a><a class="link">District Meetings</a><a class="link">Licensing Board Information</a><a class="link">Library</a><a class="link">Administrators ( DRNEV )</a><a class="link">Legal Advisors ( DRNEV )</a>
    <a class="btn">GET STARTED</a>
  </div>
  <div class="photo" role="img" aria-label="Photo of a therapist massaging the back of a patient lying on a table" style="background:linear-gradient(160deg,#e6e6e6 0%,#d4bfb2 50%,#c9c9c9 100%)"></div>
  <div class="panel">
    <h2 class="serif">Registered Chiropractors</h2>
    <a class="link">Coninuing Education Courses</a><a class="link">Chiropractic Assistant</a><a class="link">Certification</a><a class="link">View Your Continuing Ed Credits</a>
    <a class="btn">GET STARTED</a>
  </div>
</section>

<section class="contact">
  <div class="c-item" style="left:100px;top:0"><div class="ico"><svg width="22" height="22" viewBox="0 0 24 24" fill="#2e6399"><path d="M6.6 10.8c1.4 2.8 3.8 5.1 6.6 6.6l2.2-2.2c.3-.3.7-.4 1-.2 1.1.4 2.3.6 3.6.6.6 0 1 .4 1 1V20c0 .6-.4 1-1 1C10.6 21 3 13.4 3 4c0-.6.4-1 1-1h3.5c.6 0 1 .4 1 1 0 1.3.2 2.5.6 3.6.1.3 0 .7-.2 1z"/></svg></div><div><h4>Office Phone</h4><p>555.218.4400</p></div></div>
  <div class="c-item" style="left:347px;top:0"><div class="ico"><svg width="24" height="22" viewBox="0 0 24 22" fill="#2e6399"><rect x="6" y="1" width="12" height="6"/><rect x="1" y="8" width="22" height="9" rx="2"/><rect x="6" y="14" width="12" height="7" fill="#fff" stroke="#2e6399" stroke-width="2"/></svg></div><div><h4>Office Fax</h4><p>555.218.4401</p></div></div>
  <div class="c-item" style="left:594px;top:0"><div class="ico"><svg width="26" height="18" viewBox="0 0 26 18" fill="#2e6399"><path d="M0 0h26v18H0z"/><path d="M1 1l12 9 12-9M1 17l9-7M25 17l-9-7" stroke="#fff" stroke-width="1.5" fill="none"/></svg></div><div><h4>Email</h4><p>info@artmhub.org</p></div></div>
  <div class="c-item" style="left:849px;top:0"><div class="ico"><svg width="20" height="26" viewBox="0 0 20 26" fill="#2e6399"><path d="M10 0C4.5 0 0 4.3 0 9.7 0 17 10 26 10 26s10-9 10-16.3C20 4.3 15.5 0 10 0zm0 14a4.3 4.3 0 110-8.6 4.3 4.3 0 010 8.6z"/></svg></div><div><h4>Address</h4><p>2210 W. Harbor Lane, Suite<br>300</p></div></div>
</section>

<footer class="footer">
  <div class="f-brand"><div class="mark"></div><div class="name">ARTM</div></div>
  <p class="f-mission">to protect the public by promoting excellence in chiropractic regulation through service to our member boards</p>
  <div class="f-col" style="left:337px"><h5>Site Map</h5><a>- Home</a><a>- Contact</a><a>- Company Info</a><a>- Chiropractic Boards</a><a>- Resources</a><a>- Services</a><a>- Get Started</a></div>
  <div class="f-col" style="left:613px"><h5>Company</h5><a>- Contact Us</a><a>- Query MOR-TEP</a><a>- Manage VOLT Courses</a><a>- Pay Invoice</a><a>- For Our Board</a><a>- Login</a></div>
  <div class="f-col" style="left:888px">
    <h5>Contact Us</h5>
    <div class="f-sub"><svg width="20" height="14" viewBox="0 0 20 14" fill="none" stroke="#2e6399" stroke-width="1.6"><rect x="1" y="1" width="18" height="12"/><path d="M1 1l9 7 9-7"/></svg>Enter Email Adreess....</div>
    <a class="btn">GET STARTED</a>
  </div>
  <p class="copy">Copyright 2021 by ARTM | Privacy Statement | Terms Of Use</p>
  <div class="social"><span>chatterbox</span><span>flitter</span><span>workloop</span><span>snapgrid</span><span>clipstream</span></div>
</footer>

</body>
</html>
```